Copperfork Roundtable Podcast

We need a Podcast Cover design that is compatible with Apple Podcasts, Spotify, etc. In this podcast, we interview the real movers & shakers in the foodservice industry who cut through the noise to get to the top.

```html
<!DOCTYPE html>
<html lang="en">
<head>
<meta charset="utf-8">
<title>Copperfork Roundtable Podcast – Cover</title>
<link href="https://fonts.googleapis.com/css2?family=Anton&family=Arimo:wght@400&family=Great+Vibes&display=swap" rel="stylesheet">
<style>
  :root {
    --navy: #0f1d33;
    --orange: #ee6f0a;
    --orange-deep: #e0600a;
    --gold: #ffc806;
    --amber-dark: #2a1f12;
    --amber-mid: #6b5128;
    --amber-light: #b8913e;
    --white: #ffffff;
  }
  * { margin: 0; padding: 0; box-sizing: border-box; }
  html, body {
    width: 1200px;
    height: 1200px;
    overflow: hidden;
    background: #ffffff;
  }
  .cover {
    position: relative;
    width: 1200px;
    height: 1200px;
    overflow: hidden;
  }
  .cover__photo {
    position: absolute;
    inset: 0;
    background:
      radial-gradient(ellipse 380px 520px at 640px 620px, rgba(20,30,55,0.85), rgba(20,30,55,0) 75%),
      radial-gradient(ellipse 500px 260px at 330px 380px, rgba(190,170,90,0.55), rgba(190,170,90,0) 70%),
      radial-gradient(ellipse 260px 420px at 1040px 420px, rgba(210,160,70,0.5), rgba(210,160,70,0) 70%),
      linear-gradient(180deg, var(--amber-mid) 0%, var(--amber-light) 30%, var(--amber-mid) 60%, var(--amber-dark) 100%);
  }
  .title-band {
    position: absolute;
    left: 0;
    top: 509px;
    width: 1200px;
    height: 320px;
    background: linear-gradient(90deg,
      rgba(238,111,10,0) 0%,
      rgba(238,111,10,0.55) 14%,
      rgba(238,111,10,0.9) 26%,
      var(--gold) 50%,
      var(--orange) 78%,
      rgba(224,96,10,0.85) 100%);
  }
  .title {
    position: absolute;
    left: 0;
    width: 1200px;
    top: 512px;
    text-align: center;
    font-family: "Anton", "Impact", sans-serif;
    font-size: 158px;
    line-height: 152px;
    letter-spacing: -1px;
    color: var(--navy);
    text-transform: uppercase;
  }
  .title__line { display: block; padding-left: 20px; }
  .host-with {
    position: absolute;
    left: 0;
    width: 1200px;
    top: 850px;
    text-align: center;
    font-family: "Great Vibes", cursive;
    font-size: 60px;
    color: var(--white);
  }
  .host-name {
    position: absolute;
    left: 0;
    width: 1200px;
    top: 922px;
    text-align: center;
    font-family: "Arimo", Arial, sans-serif;
    font-size: 80px;
    letter-spacing: 1px;
    background: linear-gradient(90deg, var(--orange-deep) 25%, var(--gold) 50%, var(--orange) 75%);
    -webkit-background-clip: text;
    background-clip: text;
    color: transparent;
  }
</style>
</head>
<body>
  <main class="cover">
    <div class="cover__photo" role="img" aria-label="Photo of the smiling host in a navy blazer and light blue shirt, seated at a bar in a warmly lit restaurant"></div>
    <div class="title-band"></div>
    <h1 class="title">
      <span class="title__line">Copperfork</span>
      <span class="title__line">Roundtable</span>
    </h1>
    <p class="host-with">with</p>
    <p class="host-name">DARIO VELASQUEZ</p>
  </main>
</body>
</html>
```